VORIKA FLYER 2019

Hi, We need an A4 flyer design for our cleaning company, focusing on dry carpet cleaning I attached our catalogue to give some idea. In addition, our websites can provide more information. Our Services:-General Cleaning Carry out heavy cleansing tasks and special projects. Clean, stock and supply designated facility areas (dusting, sweeping, vacuuming, mopping, cleaning ceiling vents, restroom cleaning etc).Using electrically powered scrubbing and polishing machines to burnish, scrub, polish and spray clean floors. Window Cleaning Regular, Reliable Window Cleaning. Hard To Reach Windows. Single 7 Multi-Storey. Frames and Glass Cleaned. Floor Cleaning Marble Cleaning & Polishing. Tile & Grout Cleaning. Hardwood Floors Services. Vinyl Floors. The PLUME Dry Extraction Carpet Cleaning System uses environmentally preferred, Clear Leaf Certified cleaning products that deep cleans your carpets and textured hard floors quickly and easily.

Target Market(s)

Residential and Commercial.
Offices, Hospitals, Restaurants, Etc.

Industry/Entity Type

Cleaning Service

Font styles to use
Serif
Sans Serif

Colors
33a6d7
0592cd
85cae6
85acd3
3277b5
296eb1

Requirements
Must have
• CREATIVE AND MINIMAL
Nice to have
• Engaging Pics and Texts

```html
<!DOCTYPE html>
<html lang="en">
<head>
<meta charset="utf-8">
<title>Vorika Cleaning &amp; Maintenance Flyer</title>
<link href="https://fonts.googleapis.com/css2?family=Roboto+Condensed:wght@700&family=Ubuntu:wght@500;700&family=Montserrat:wght@400&display=swap" rel="stylesheet">
<style>
  :root {
    --sky: #33a6d7;
    --azure: #0592cd;
    --band: #1b8fd0;
    --pale: #85cae6;
    --mist: #85acd3;
    --royal: #3277b5;
    --deep: #296eb1;
    --navy: #2b2b6a;
    --paper: #ffffff;
    --soft: #f2f3f6;
    --canvas: #e9ecf0;
    --ink: #2a2d36;
  }
  * { box-sizing: border-box; margin: 0; padding: 0; }
  html, body { width: 1200px; height: 1200px; overflow: hidden; background: var(--canvas); }
  .flyer {
    position: absolute; left: 186px; top: 20px; width: 828px; height: 1160px;
    background: var(--paper); overflow: hidden;
    box-shadow: 0 4px 18px rgba(0,0,0,.15);
  }
  .top-bar { position: absolute; left: 0; top: 0; width: 100%; height: 21px; background: var(--royal); }

  .brand { position: absolute; left: 30px; top: 78px; display: flex; align-items: center; gap: 14px; }
  .brand-mark { width: 22px; height: 22px; background: var(--royal); flex: none; }
  .brand-name { font-family: 'Ubuntu', sans-serif; font-weight: 500; font-size: 30px; line-height: 1.15; color: var(--navy); }

  .headline { position: absolute; left: 27px; top: 226px; font-family: 'Roboto Condensed', sans-serif; font-weight: 700; line-height: .88; }
  .headline-kicker { font-family: 'Ubuntu', sans-serif; font-weight: 700; font-size: 36px; color: var(--sky); letter-spacing: .5px; display: block; margin-bottom: 14px; }
  .headline-main { font-size: 94px; color: var(--deep); display: block; letter-spacing: -1px; }

  .team-photo {
    position: absolute; left: 415px; top: 112px; width: 413px; height: 480px;
    background: radial-gradient(ellipse at 50% 45%, #bfe1f2 0%, #e4f2fa 55%, #ffffff 80%);
  }

  .services-band { position: absolute; left: 0; top: 566px; width: 100%; height: 268px; background: var(--band); }

  .snapshot { position: absolute; background: var(--paper); padding: 8px; box-shadow: 0 3px 8px rgba(0,0,0,.25); }
  .snapshot-fill { width: 100%; height: 100%; }
  .snap-carpet { left: 30px; top: 510px; width: 190px; height: 200px; transform: rotate(-25deg); }
  .snap-carpet .snapshot-fill { background: linear-gradient(160deg, #b7a893, #8a8378); }
  .snap-windows { left: 224px; top: 488px; width: 188px; height: 190px; transform: rotate(1deg); }
  .snap-windows .snapshot-fill { background: linear-gradient(180deg, #8595ab, #4f5f78); }
  .snap-restroom { left: 418px; top: 510px; width: 190px; height: 190px; transform: rotate(30deg); }
  .snap-restroom .snapshot-fill { background: linear-gradient(135deg, #e8e6e2, #d9b66a); }
  .snap-floor { left: 586px; top: 506px; width: 210px; height: 205px; transform: rotate(8deg); }
  .snap-floor .snapshot-fill { background: linear-gradient(180deg, #c9d4cc, #9aa3a4); }

  .services-title { position: absolute; left: 0; top: 709px; width: 100%; text-align: center; font-family: 'Ubuntu', sans-serif; font-weight: 500; font-size: 29px; color: var(--paper); }
  .services-copy { position: absolute; left: 25px; top: 765px; width: 778px; text-align: center; font-family: 'Montserrat', sans-serif; font-size: 13.2px; line-height: 16.4px; color: var(--paper); }

  .why-section { position: absolute; left: 0; top: 834px; width: 100%; height: 262px; background: var(--soft); }
  .why-title { position: absolute; left: 0; top: 862px; width: 100%; text-align: center; font-family: 'Ubuntu', sans-serif; font-weight: 500; font-size: 30px; color: var(--deep); }
  .feature { position: absolute; top: 928px; }
  .feature-icon { display: block; height: 48px; margin-bottom: 26px; }
  .feature-text { font-family: 'Montserrat', sans-serif; font-size: 13.2px; line-height: 16.4px; color: var(--ink); text-align: justify; }
  .feature-window { left: 26px; width: 214px; }
  .feature-window .feature-icon { margin-left: 74px; }
  .feature-carpet { left: 272px; width: 288px; }
  .feature-carpet .feature-icon { margin-left: 106px; }
  .feature-floor { left: 587px; width: 214px; }
  .feature-floor .feature-icon { margin-left: 76px; }
  .divider { position: absolute; top: 928px; width: 2px; height: 158px; background: var(--sky); }
  .divider-a { left: 256px; }
  .divider-b { left: 572px; }

  .footer { position: absolute; left: 0; top: 1096px; width: 100%; height: 64px; background: var(--royal); display: flex; align-items: center; justify-content: center; }
  .footer-url { font-family: 'Ubuntu', sans-serif; font-weight: 500; font-size: 22px; letter-spacing: 2.4px; color: var(--paper); }
</style>
</head>
<body>
<main class="flyer">
  <div class="top-bar"></div>

  <header class="brand">
    <span class="brand-mark"></span>
    <div class="brand-name">Vorika Cleaning<br>&amp; Maintenance</div>
  </header>

  <h1 class="headline">
    <span class="headline-kicker">PROFESSIONAL</span>
    <span class="headline-main">CLEANING</span>
    <span class="headline-main">SERVICES</span>
  </h1>

  <div class="team-photo" role="img" aria-label="Three cleaning staff in blue aprons with a vacuum, mop, cart and wet floor sign"></div>

  <section class="services-band"></section>

  <div class="snapshot snap-carpet"><div class="snapshot-fill" role="img" aria-label="Floor scrubbing machine on a carpet"></div></div>
  <div class="snapshot snap-windows"><div class="snapshot-fill" role="img" aria-label="Rope access worker cleaning high-rise windows"></div></div>
  <div class="snapshot snap-restroom"><div class="snapshot-fill" role="img" aria-label="Gloved hands wiping a restroom fixture"></div></div>
  <div class="snapshot snap-floor"><div class="snapshot-fill" role="img" aria-label="Polishing machine cleaning a hard floor"></div></div>

  <h2 class="services-title">Our Services:</h2>
  <p class="services-copy">General Cleaning Carry out heavy cleansing tasks and special projects. Clean, stock and supply designated facility areas (dusting, sweeping, vacuuming, mopping, cleaning ceiling vents, restroom cleaning etc).Using electrically powered scrubbing and polishing machines to burnish, scrub, polish and spray clean floors.</p>

  <section class="why-section"></section>
  <h2 class="why-title">Why Choose Us:</h2>

  <div class="feature feature-window">
    <svg class="feature-icon" width="52" height="48" viewBox="0 0 52 48" fill="none" stroke="#3277b5" stroke-width="2">
      <rect x="3" y="2" width="46" height="42"/>
      <line x1="26" y1="2" x2="26" y2="44"/>
      <rect x="7" y="6" width="15" height="34"/>
      <rect x="30" y="6" width="15" height="34"/>
      <line x1="1" y1="46" x2="51" y2="46"/>
      <line x1="34" y1="34" x2="44" y2="20"/>
    </svg>
    <p class="feature-text">Window Cleaning Regular, Reliable Window Cleaning. Hard To Reach Windows. Single 7 Multi-Storey. Frames and Glass Cleaned.</p>
  </div>
  <div class="divider divider-a"></div>

  <div class="feature feature-carpet">
    <svg class="feature-icon" width="54" height="48" viewBox="0 0 54 48" fill="none" stroke="#3277b5" stroke-width="2">
      <rect x="14" y="6" width="38" height="36"/>
      <rect x="17" y="9" width="32" height="30" stroke-dasharray="2 2"/>
      <rect x="4" y="2" width="8" height="44"/>
      <line x1="12" y1="24" x2="16" y2="24"/>
      <circle cx="8" cy="8" r="2"/>
      <circle cx="8" cy="40" r="2"/>
    </svg>
    <p class="feature-text">The PLUME Dry Extraction Carpet Cleaning System uses environmentally preferred, Clear Leaf Certified cleaning products that deep cleans your carpets and textured hard floors quickly and easily.</p>
  </div>
  <div class="divider divider-b"></div>

  <div class="feature feature-floor">
    <svg class="feature-icon" width="62" height="48" viewBox="0 0 62 48" fill="none" stroke="#3277b5" stroke-width="2.4">
      <rect x="14" y="4" width="26" height="8" rx="2"/>
      <rect x="10" y="14" width="34" height="16"/>
      <line x1="18" y1="19" x2="18" y2="26"/>
      <line x1="24" y1="19" x2="24" y2="26"/>
      <line x1="30" y1="19" x2="30" y2="26"/>
      <line x1="36" y1="19" x2="36" y2="26"/>
      <path d="M4 34 H58 a4 4 0 0 1 0 8 H4 a4 4 0 0 1 0 -8z"/>
      <path d="M44 22 H56 a3 3 0 0 1 0 6 H44"/>
    </svg>
    <p class="feature-text">Floor Cleaning Marble Cleaning &amp; Polishing. Tile &amp; Grout Cleaning. Hardwood Floors Services. Vinyl Floors.</p>
  </div>

  <footer class="footer"><span class="footer-url">www.vorikaclean.com</span></footer>
</main>
</body>
</html>
```